Construction Company business card and Logo.

We need a business card for a Building Company.
We build and constuction manage.
A simple logo is also required. Ive attached some samples that may assist.
Logo colours: Blue,sunburnt orange,lime/green and brown/grey.
The Font for the Brevanta logo ive been using is Georgia.
Maybe the A in Brevanta can be like my logo design..?
All other font either calibri or arial, something simple.
Simple/modern and neat is what i am looking for.
My card should look organised to convey what the company is about.

Target Market(s)

Developers, architects, proffesionals in general

Industry/Entity Type

Business

Contact Information for Business Card

Brevanta Constructions Pty Ltd
ACN: 381 607 925 Lic:716382D
Dermot Halvorsen
Managing Director
0438 215 706
dermot@brevanta.com.au
www.brevanta.com.au
Industrial.Commercial.Residential.Build Management

Requirements
Must have
• Ive attached some ideas for the logo. Its simple. If you come up with something else, please show me as im not 100% sure of what i want.
The front of the card should be white.
The back of the card should have the company name and logo with Blue background
Should not have
• the design should be simple.
No old style fonts or italics etc

```html
<!DOCTYPE html>
<html lang="en">
<head>
<meta charset="utf-8">
<title>Brevanta Constructions – Business Card</title>
<link href="https://fonts.googleapis.com/css2?family=Open+Sans:wght@400;600;700&display=swap" rel="stylesheet">
<style>
  :root{
    --backdrop:#4a4a4c;
    --card-white:#f4f4f3;
    --ink:#4b4b4d;
    --ink-soft:#5a5a5c;
    --ink-faint:#a5a5a5;
    --link-blue:#1f5f9c;
    --band:#4e4e50;
    --band-text:#f1f1f1;
    --blue-deep:#0a3577;
    --blue-mid:#0f8fc0;
    --blue-light:#5aaac8;
    --lime:#a5c21b;
    --white:#ffffff;
  }
  *{margin:0;padding:0;box-sizing:border-box}
  html,body{width:1200px;height:1000px;overflow:hidden}
  body{background:var(--backdrop);font-family:"Open Sans",Arial,sans-serif;position:relative}

  .card{position:absolute;width:528px;height:300px;border-radius:14px;overflow:hidden}

  /* Front */
  .card-front{left:207px;top:165px;background:var(--card-white);color:var(--ink)}
  .brand{position:absolute;left:48px;top:58px;display:flex;align-items:flex-start;gap:10px}
  .brand-mark{width:22px;height:22px;background:var(--lime);margin-top:10px}
  .brand-name{font-weight:700;color:var(--ink);line-height:1.05;text-transform:uppercase}
  .brand-name .brand-main{display:block;font-size:34px;letter-spacing:.5px}
  .brand-name .brand-sub{display:block;font-size:13px;letter-spacing:.2px;margin-top:4px}

  .web{position:absolute;right:306px;top:208px;font-size:13px;color:var(--ink-soft);text-align:right}
  .web .web-name{color:var(--link-blue);font-size:15px}
  .reg{position:absolute;right:308px;top:234px;font-size:8px;color:var(--ink-faint);letter-spacing:.3px;white-space:nowrap}

  .contact{position:absolute;left:314px;top:98px;font-size:12.5px;color:var(--ink-soft);line-height:1.45}
  .person-name{font-size:16px;font-weight:700;color:var(--ink);letter-spacing:.4px;text-transform:uppercase;line-height:1.2}
  .person-role{margin-bottom:16px}
  .contact .label{font-weight:700;color:var(--ink)}
  .address{margin-top:18px}

  .services{position:absolute;left:0;bottom:0;width:100%;height:33px;background:var(--band);color:var(--band-text);
    font-size:16px;text-align:center;line-height:33px;letter-spacing:.1px;padding-left:12px}

  /* Back */
  .card-back{left:472px;top:534px;
    background:linear-gradient(115deg,var(--blue-deep) 0%,var(--blue-deep) 12%,var(--blue-mid) 55%,var(--blue-light) 100%);
    color:var(--white)}
  .card-back .brand{left:0;top:0;width:100%;height:100%;justify-content:center;align-items:center;gap:12px}
  .card-back .brand-name{color:var(--white);text-align:left}
</style>
</head>
<body>

  <section class="card card-front" aria-label="Business card front">
    <div class="brand">
      <span class="brand-mark"></span>
      <div class="brand-name"><span class="brand-main">Brevanta</span><span class="brand-sub">Constructions Pty Ltd</span></div>
    </div>

    <p class="web">www.<span class="web-name">brevanta</span>.com.au</p>
    <p class="reg">ACN: 381 607 925&nbsp;&nbsp;&nbsp;LIC: 716382D</p>

    <div class="contact">
      <p class="person-name">Dermot Halvorsen</p>
      <p class="person-role">Managing Director</p>
      <p><span class="label">Mob:</span> 0438-215-706</p>
      <p><span class="label">Email:</span> dermot@brevanta.com.au</p>
      <p class="address">217 Ashgrove Road<br>Mount Ellery Victoria 315</p>
    </div>

    <p class="services">Industrial • Commercial • Residential • Build Management</p>
  </section>

  <section class="card card-back" aria-label="Business card back">
    <div class="brand">
      <span class="brand-mark"></span>
      <div class="brand-name"><span class="brand-main">Brevanta</span><span class="brand-sub">Constructions Pty Ltd</span></div>
    </div>
  </section>

</body>
</html>
```